Business cards for the RL Group

We are looking for a template for our new business cards for our company that we can edit ourselves.
You will find our company colors in the logo. the logo on the back and on the front
first name Last Name
position
E-mail address
mobile number
landline number
Companies we have 2 RL Sicherheit GmbH and RL Services GmbH
address
Lindenbergweg 42
22459 Hamburg
www.rlgruppe-nord.de

Something modern, simple but professional

if you have any questions, bring it on.

Sicherheit

Steht in der Beschreibung

F0912C
F2A743
F7CA91
FBE8D2
FDF5EE

• recognition value
• professional
• Playful

```html
<!DOCTYPE html>
<html lang="de">
<head>
<meta charset="utf-8">
<title>RL Gruppe – Visitenkarten</title>
<link rel="stylesheet" href="https://fonts.googleapis.com/css2?family=Poppins:wght@500;600&display=swap">
<style>
  :root {
    --bg: #b9b5b1;
    --orange: #f47b20;
    --slate: #555658;
    --card-dark: #5e5e5e;
    --ink: #4a4a4a;
    --white: #ffffff;
  }
  * { margin: 0; padding: 0; box-sizing: border-box; }
  html, body { width: 1200px; height: 2342px; overflow: hidden; }
  body {
    background: var(--bg);
    font-family: "Poppins", sans-serif;
    position: relative;
  }
  .card {
    position: absolute;
    left: 150px;
    width: 900px;
    height: 512px;
    box-shadow: 0 14px 34px rgba(0,0,0,0.28);
    overflow: hidden;
  }
  .card--front { top: 590px; background: var(--white); border: 7px solid var(--orange); }
  .card--back { top: 1230px; background: var(--card-dark); }

  .front-accents { position: absolute; inset: 0; width: 100%; height: 100%; }

  .brand {
    position: absolute;
    display: flex;
    align-items: center;
    gap: 14px;
    font-weight: 600;
    color: var(--slate);
    letter-spacing: 0.5px;
    white-space: nowrap;
    line-height: 1;
  }
  .brand__dot { border-radius: 50%; background: var(--orange); flex: none; }
  .card--front .brand { left: 117px; top: 64px; font-size: 52px; }
  .card--front .brand__dot { width: 30px; height: 30px; }
  .card--back .brand {
    left: 50%; top: 50%; transform: translate(-50%, -50%);
    font-size: 84px; color: var(--orange);
  }
  .card--back .brand__dot { width: 44px; height: 44px; }

  .person { position: absolute; left: 117px; top: 146px; color: var(--slate); }
  .person__name { font-weight: 600; font-size: 20px; line-height: 26px; }
  .person__role { font-weight: 500; font-size: 15px; line-height: 20px; color: var(--ink); }

  .companies {
    position: absolute; left: 117px; top: 212px;
    color: var(--orange); font-weight: 600; font-size: 19.5px; line-height: 26px;
  }
  .contact-list {
    position: absolute; left: 117px; top: 284px;
    list-style: none; color: var(--ink); font-weight: 500; font-size: 16px; line-height: 22px;
  }
  .contact-list li { display: flex; align-items: flex-start; gap: 22px; }
  .contact-list li + li { margin-top: 2px; }
  .contact-list .label { color: var(--orange); font-weight: 600; margin-right: 6px; }
  .icon { width: 18px; height: 18px; flex: none; margin-top: 2px; fill: var(--orange); }
  .footer-row {
    position: absolute; left: 322px; right: 40px; top: 448px;
    display: flex; justify-content: space-between; align-items: center;
    color: var(--ink); font-weight: 500; font-size: 15.5px;
  }
  .footer-row span { display: flex; align-items: center; gap: 20px; }
</style>
</head>
<body>

<section class="card card--front" aria-label="Vorderseite">
  <svg class="front-accents" viewBox="0 0 886 498" preserveAspectRatio="none" aria-hidden="true">
    <polygon points="650,0 886,0 886,50" fill="#555658"/>
    <polygon points="650,0 886,0 886,36" fill="#f47b20"/>
    <polygon points="0,420 250,478 0,478" fill="#555658"/>
    <polygon points="0,436 250,478 0,478" fill="#f47b20"/>
    <polygon points="0,478 886,478 886,498 0,498" fill="#f47b20"/>
  </svg>

  <div class="brand"><span class="brand__dot"></span>RL Gruppe</div>

  <div class="person">
    <p class="person__name">Vorname Nachname</p>
    <p class="person__role">Position</p>
  </div>

  <p class="companies">2 RL SICHERHEIT GMBH &amp;<br>RL SERVICES GMBH</p>

  <ul class="contact-list">
    <li>
      <svg class="icon" viewBox="0 0 24 24"><path d="M7 2h10a1 1 0 0 1 1 1v18a1 1 0 0 1-1 1H7a1 1 0 0 1-1-1V3a1 1 0 0 1 1-1zm1 3v13h8V5zm4 14.2a1 1 0 1 0 0 2 1 1 0 0 0 0-2z"/></svg>
      <span><span class="label">Mobil</span>0170 1234567</span>
    </li>
    <li>
      <svg class="icon" viewBox="0 0 24 24"><path d="M6.6 10.8c1.4 2.8 3.8 5.1 6.6 6.6l2.2-2.2c.3-.3.7-.4 1-.2 1.1.4 2.3.6 3.6.6.6 0 1 .4 1 1V20c0 .6-.4 1-1 1C10.6 21 3 13.4 3 4c0-.6.4-1 1-1h3.5c.6 0 1 .4 1 1 0 1.3.2 2.5.6 3.6.1.3 0 .7-.2 1z"/></svg>
      <span><span class="label">Festnetz</span>040 1234567</span>
    </li>
    <li>
      <svg class="icon" viewBox="0 0 24 24"><path d="M12 2C8.1 2 5 5.1 5 9c0 5.2 7 13 7 13s7-7.8 7-13c0-3.9-3.1-7-7-7zm0 9.5A2.5 2.5 0 1 1 12 6.5a2.5 2.5 0 0 1 0 5z"/></svg>
      <span>Lindenbergweg 42<br>22459 Hamburg</span>
    </li>
  </ul>

  <div class="footer-row">
    <span>
      <svg class="icon" viewBox="0 0 24 24"><path d="M2 5h20v14H2zM3.5 6.5 12 13l8.5-6.5" fill="none" stroke="#f47b20" stroke-width="2"/></svg>
      kontakt@rlgruppe-nord.de
    </span>
    <span>
      <svg class="icon" viewBox="0 0 24 24"><g fill="none" stroke="#f47b20" stroke-width="1.8"><circle cx="12" cy="12" r="9"/><ellipse cx="12" cy="12" rx="4" ry="9"/><path d="M3 12h18M5 7h14M5 17h14"/></g></svg>
      www.rlgruppe-nord.de
    </span>
  </div>
</section>

<section class="card card--back" aria-label="Rückseite">
  <div class="brand"><span class="brand__dot"></span>RL Gruppe</div>
</section>

</body>
</html>
```